Meadowbrook Wellbeing Practice Kestrel

We need a design for magazine advert, ideally high resolution to advertise our counselling centre. we would like this to include a photo of two people talking, as if in a counselling session. See our logo and colour range on our website. www.mwpk-kestrel.co.uk
The photo should not include cups of coffee, clipboards, desks, people touching. it needs to be two people in armchairs sympathetically listening and looking at each other.
The font type is Great Vibes on the logo. Our design should communicate a centre of excellence delivering high quality, professional services in stylishly furnished surroundings.

Hello Everyone We have had a number of designs that look quite promising but are missing the brief. Can I reiterate that we need a photograph of 2 people seated talking to each other in a sincere way. There shouldn't be office chairs but comfortable chairs. There should be no physical contact. There should be no clipboards.Thank you very muchHeather Added Sunday, March 12, 2017

Target Market(s)

people seeking counselling and psychotherapy

Font styles to use
Other font styles liked:
• Great Vibes as in our logo for some of the print. See attached file.

Requirements
Must have
• good photograph
• Two high res Pixelgrove photos:
• https://pixelgrove-files.example-mail.net/download?q=Xb71KmPq9TzRw2VnLc8HdY4sFjA3uE6oG0iN5tQ1rWvZx7KmBp2NcD8LhS3fJg%3D%3D
• https://pixelgrove-files.example-mail.net/download?q=Xb71KmPq9TzRw2VnLc8HdT6yMeQ4pW9aJ3kR1uZ0sNvH5bG2xLcF7oD8iY4tAwEe%3D%3D
Nice to have
• Watermark in keeping with our logo.
Should not have
• Darkness

```html
<!DOCTYPE html>
<html lang="en">
<head>
<meta charset="utf-8">
<title>Meadowbrook Wellbeing Practice – Magazine Advert</title>
<link rel="stylesheet" href="https://fonts.googleapis.com/css2?family=Great+Vibes&family=Tenor+Sans&family=Crimson+Text:wght@700&display=swap">
<style>
  :root {
    --backdrop: #e6e6e6;
    --paper: #ffffff;
    --olive: #86913a;
    --sage: #6e8f55;
    --ink: #1d1a1a;
    --brand-ink: #2d1c1e;
    --footer: #231f20;
    --footer-text: #ffffff;
  }
  * { box-sizing: border-box; margin: 0; padding: 0; }
  html, body { width: 1200px; height: 1200px; overflow: hidden; background: var(--backdrop); }
  .advert {
    position: absolute; left: 190px; top: 24px;
    width: 910px; height: 1280px;
    background: var(--paper);
    transform: scale(0.9); transform-origin: top left;
    font-family: "Tenor Sans", sans-serif; color: var(--ink);
  }
  .brand {
    position: absolute; top: 110px; left: 0; right: 0;
    display: flex; justify-content: center; align-items: center; gap: 16px;
    font-family: "Great Vibes", cursive; font-size: 58px; color: var(--brand-ink);
    z-index: 2;
  }
  .brand-dot { width: 18px; height: 18px; border-radius: 50%; background: var(--sage); }
  .session-photo {
    position: absolute; top: 200px; left: 0; width: 910px; height: 472px;
    background: linear-gradient(180deg, #ffffff 0%, #e9eef0 22%, #d3dcdf 55%, #b9a894 78%, #f0f0ee 100%);
  }
  .quote-band {
    position: absolute; top: 672px; left: 0; width: 910px; height: 146px;
    background: var(--olive); color: #fff;
    font-size: 27px; line-height: 35px; text-align: center;
    padding-top: 42px;
  }
  .quote-mark { font-family: Georgia, serif; font-weight: bold; font-size: 62px; line-height: 0; position: relative; }
  .quote-mark.open { top: 14px; margin-right: 6px; }
  .quote-mark.close { top: 36px; margin-left: 14px; }
  .therapist { position: absolute; top: 836px; width: 100%; text-align: center; font-size: 35px; }
  .tagline {
    position: absolute; top: 880px; width: 100%; text-align: center;
    font-family: "Great Vibes", cursive; font-size: 64px; line-height: 78px; color: var(--sage);
  }
  .services { position: absolute; top: 1052px; width: 100%; text-align: center; font-size: 22.5px; line-height: 31px; }
  .hours { position: absolute; top: 1130px; width: 100%; text-align: center; font-size: 24px; }
  .contact-bar {
    position: absolute; top: 1190px; left: 2px; width: 906px; height: 88px;
    background: var(--footer); color: var(--footer-text);
    font-family: "Crimson Text", serif; font-weight: 700;
  }
  .address { position: absolute; left: 52px; top: 36px; font-size: 20px; }
  .divider { position: absolute; left: 495px; top: 10px; width: 1px; height: 72px; background: #bbb; }
  .phone, .web { position: absolute; left: 546px; display: flex; align-items: center; gap: 12px; }
  .phone { top: 6px; font-family: "Tenor Sans", sans-serif; font-weight: 400; font-size: 39px; letter-spacing: 1px; }
  .web { top: 52px; font-size: 23px; }
  .icon { width: 22px; height: 22px; }
</style>
</head>
<body>
<main class="advert">
  <header class="brand"><span class="brand-dot"></span><span>Meadowbrook Wellbeing Practice</span></header>

  <div class="session-photo" role="img" aria-label="Photograph of two people seated facing each other in conversation beside a bright window"></div>

  <blockquote class="quote-band">
    <span class="quote-mark open">“</span>A big part of letting go is recognising when it is time to<br>
    stay in a situation and when it is time to move on<span class="quote-mark close">”</span>
  </blockquote>

  <p class="therapist">Martin R.Hale</p>
  <h1 class="tagline">Confidental Therapentic Services<br>in the Heart of Old Town</h1>

  <p class="services">We Have Over 30 Carefully Selected, Qualitied And Professional Therapists<br>Offering A Range Of Services To Help Individuals,familyes And Couples</p>
  <p class="hours">Appointments available throughout the day and evening</p>

  <footer class="contact-bar">
    <span class="address">14 Mill Lane,Old Quarter,Kestrel KS1 4AB</span>
    <span class="divider"></span>
    <span class="phone">
      <svg class="icon" viewBox="0 0 24 24"><path fill="#8da15a" d="M6.6 10.8a15 15 0 0 0 6.6 6.6l2.2-2.2c.3-.3.7-.4 1-.2 1.1.4 2.3.6 3.6.6.6 0 1 .4 1 1V20c0 .6-.4 1-1 1A17 17 0 0 1 3 4c0-.6.4-1 1-1h3.5c.6 0 1 .4 1 1 0 1.3.2 2.5.6 3.6.1.3 0 .7-.2 1z"/></svg>
      01632960418
    </span>
    <span class="web">
      <svg class="icon" viewBox="0 0 24 24" fill="none" stroke="#8da15a" stroke-width="1.6"><circle cx="12" cy="12" r="9.5"/><ellipse cx="12" cy="12" rx="4" ry="9.5"/><path d="M2.5 12h19M4 7h16M4 17h16"/></svg>
      www.mwpk-kestrel.co.uk
    </span>
  </footer>
</main>
</body>
</html>
```